■依頼の目的/概要
ベストセラー作家が送る最新作の表紙を飾りませんか?
Borelo QuillのBWSの電子書籍表紙デザインをお願いします。

■本の内容
*タイトル:
うつむく朝に灯すひと匙の言葉

というタイトルの表紙デザインの発注になります。

■デザイン要望

要望1つ目
作家名は後でお伝えします。作家名もどこかに挿入いただきたいです。よろしくお願いします。
提出の際は ○○著という形でご提出よろしくお願いします。

要望2つ目
ウェルネスバランスコーチ検定資格保持者

とどこかに入れてください。

要望3つ目
累計Borelo 1位〇冠
(現在、59冠までいっています。今後、出版が控えている作品があります。
そのため、その最終冠数を入れて頂きたいです。)

とどこかに入れてください。

また、出来上がったデザインを作家グループの中で投票にかけて、
一番投票得票数の多かったものを表紙デザインとして選ばせていただきたいと考えております。
もしかしたら、その中で、何か修正依頼など来るかもしれませんが、
それも含めて、ご対応していただける方よろしくお願いします。

また、最終、選考後、
累計Borelo 1位〇〇冠   と記載された表紙と、
累計Borelo 1位〇〇冠   と記載されない表紙の
2表紙の納品をよろしくお願いします。他の部分の表紙のデザイン変更は不要です。
(これは、最終選ばれたデザイナーさんのみご対応で大丈夫です。)

お手数をおかけしますが、よろしくお願いします。

1部内容の抜粋を記載します。

データサイズですが、推奨サイズでJPEGファイルでご納品下さい、よろしくお願いします。
(推奨サイズは2560×1600pxです。)
その他何かご不明な点がございましたら、お気軽にご質問下さい。
よろしくお願いいたします。
変更点がでてきました。

累計Borelo 1位〇〇冠→累計Borelo 1位65冠
と決定しました。最終、この数字でご納品ください。

もうすでに提出済みの方に関しましては、当選後のご対応で大丈夫です。
お手数をおかけしますが、ご対応なにとぞよろしくお願いいたします。
皆様、たくさんのご応募まことにありがとうございました。
コンペというとても厳しい条件にも関わらず、挑戦いただいたことに
大変大変感謝しております。
ご提案されましたすべての作品、デザイナー様のご経歴、作成への思い入れ、
すべてを拝見させていただきました。
これから、作家グループへ全体回覧のメールを致します。
作家グループの皆様の投票結果までお待ちください(場合により結果
公表まで1週間から10日ぐらいかかる場合もあると思われます)。
また、この度、いろいろな作品に触れさせていただきましたこと本当に
本当に感謝いたします。
皆さまのご努力、精進そしてそのチャレンジに大変感謝と尊敬を感じております。
ご経歴やデザイナー様の名前などすべて伏せて、作品のみの提示にて
小説家作家グループに提案させていただきたいと思っております。
ただ、今回の表紙に関しましては、どうしても1名しか選べない状況がございますこと
また、総選挙による投票にて決定致しますこと、ご理解何卒よろしくお願い申しあげます。
また、もしも、今回当選に至らないことがありましても、
今後も私自身は作家生活を継続予定ですので、
(今回は作品の表紙に合わないことがあっても)作風の気に入ったデザイナー様には
個人的にお話を相談させていただく場合もあると思っております。
また、別の作品の表紙を飾っていただく可能性もあるかと思っております。
この度は誠に誠にありがとうございました。
表紙ですが、最終選考決定いたしました。
当選された方には個別に連絡をさせていただきました。

皆様からのご提案、そして、そのチャレンジに敬意と感謝をしております。
私はこれからも作家活動を継続致しますので、また、ご一緒にお仕事をさせていただき
表紙を飾っていただく機会もあるかと思います。
その際はなにとぞよろしくお願いもうしあげます。
自分のためだけでなく、ベストセラーを取り続けることで、素晴らしい表紙を飾れるチャンスをこれからも作りたいと思い、また、精進していきたいと思います。
この度はまことにありがとうございました。

「目が惹きつけられました」とか
これから上を向いて、光を見て行こうとする視線と深く、それでいて爽やかなブルーのタッチがとても印象的で綺麗‼️
など目が離せない、というようなコメントを多くいただきました。
ご提出誠にありがとうございます。

コンペについてはとても厳しい条件にも関わらず挑戦していただき、
本当に一つのタイトルに対する皆様の創造力について驚きや才能についてをいつも
感じています。
そして、そのチャレンジする姿勢にいつもエネルギーをいただき、
私自身もこれからも、いろいろなことに挑戦する姿勢を続けていきたいな、
と感じております。
表紙を飾っていただく機会もあるかと思います。
その際はなにとぞよろしくお願いもうしあげます。この度はありがとうございました。

```html
<!DOCTYPE html>
<html lang="ja">
<head>
<meta charset="UTF-8">
<title>うつむく朝に灯すひと匙の言葉</title>
<link rel="stylesheet" href="https://fonts.googleapis.com/css2?family=M+PLUS+Rounded+1c:wght@500;700;800&family=Zen+Maru+Gothic:wght@500;700&display=swap">
<style>
  :root {
    --navy: #2c2f6e;
    --orange: #f0a431;
    --cream: #f3eee3;
    --white: #ffffff;
    --pink: #f2bfbd;
    --art-a: #a9c8cf;
    --art-b: #e9d3cf;
    --gold-a: #f7dc83;
    --gold-b: #d9a83a;
    --red: #c0392b;
  }
  * { margin: 0; padding: 0; box-sizing: border-box; }
  html, body { width: 750px; height: 1200px; overflow: hidden; background: var(--cream); }
  .cover {
    position: relative; width: 750px; height: 1200px; overflow: hidden;
    background: var(--cream);
    font-family: "Zen Maru Gothic", "M PLUS Rounded 1c", sans-serif;
    color: var(--navy);
  }
  .top-band { position: absolute; left: 0; top: 0; width: 750px; height: 312px; background: var(--orange); }
  .title-panel { position: absolute; left: 55px; top: 70px; width: 640px; height: 260px; background: var(--cream); }
  .title-sub {
    position: absolute; left: 0; top: 88px; width: 750px; text-align: center;
    font-family: "M PLUS Rounded 1c", sans-serif; font-weight: 800; font-size: 44px; letter-spacing: 2px;
  }
  .title-main {
    position: absolute; left: 0; top: 140px; width: 750px; text-align: center;
    font-family: "M PLUS Rounded 1c", sans-serif; font-weight: 800; font-size: 98px; line-height: 1.1; letter-spacing: 2px;
  }
  .title-main .small { font-size: 58px; }
  .illustration {
    position: absolute; left: 100px; top: 335px; width: 550px; height: 345px;
    border-radius: 24px;
    background: linear-gradient(135deg, var(--art-b) 0%, var(--art-a) 55%, var(--art-b) 100%);
  }
  .topic-tag {
    position: absolute; left: 188px; top: 672px; padding: 6px 22px;
    background: var(--cream); border: 3px solid var(--pink); border-radius: 10px;
    font-family: "M PLUS Rounded 1c", sans-serif; font-weight: 700; font-size: 30px;
  }
  .credential {
    position: absolute; left: 0; top: 780px; width: 750px; text-align: center;
    font-family: "M PLUS Rounded 1c", sans-serif; font-weight: 800; font-size: 30px;
  }
  .author {
    position: absolute; left: 0; top: 822px; width: 750px; text-align: center;
    font-family: "M PLUS Rounded 1c", sans-serif; font-weight: 800; font-size: 28px; letter-spacing: 2px;
  }
  .bottom-band { position: absolute; left: 0; top: 875px; width: 750px; height: 325px; background: var(--orange); }
  .blurb-box {
    position: absolute; left: 22px; top: 900px; width: 706px; height: 278px; background: var(--white);
    padding: 36px 30px; font-size: 22px; font-weight: 500; line-height: 1.6;
  }
  .blurb-box p.closing { margin-top: 18px; }
  .rank-badge { position: absolute; left: 585px; top: 962px; width: 140px; height: 140px; }
</style>
</head>
<body>
<div class="cover">
  <div class="top-band"></div>
  <div class="title-panel"></div>
  <h1>
    <span class="title-sub">うつむく朝に灯す</span>
    <span class="title-main">ひと匙<span class="small">の</span>言葉</span>
  </h1>

  <div class="illustration" role="img" aria-label="ハート形の地球を二人の人物が抱きしめるイラスト"></div>

  <div class="topic-tag">#落ち込む理由</div>

  <p class="credential">ウェルネスバランスコーチ検定資格保持者</p>
  <p class="author">○○○ ○○ 著</p>

  <div class="bottom-band"></div>
  <div class="blurb-box">
    <p>人間関係、恋愛のこと、仕事のこと、<br>お金のこと、家族のこと、友人のこと、<br>自分自身のこと<br>考えることがいっぱいあります。</p>
    <p class="closing">落ち込んだときの「ヒント」を提案します!</p>
  </div>

  <svg class="rank-badge" viewBox="0 0 180 180">
    <defs>
      <radialGradient id="goldFill" cx="0.4" cy="0.35" r="0.7">
        <stop offset="0" stop-color="var(--gold-a)"/>
        <stop offset="1" stop-color="var(--gold-b)"/>
      </radialGradient>
    </defs>
    <circle cx="90" cy="90" r="88" fill="url(#goldFill)"/>
    <circle cx="90" cy="90" r="76" fill="none" stroke="#fff3c8" stroke-width="2"/>
    <text x="90" y="74" text-anchor="middle" font-family="M PLUS Rounded 1c, sans-serif" font-weight="800" font-size="22" fill="var(--navy)">累計Borelo</text>
    <text x="90" y="122" text-anchor="middle" font-family="M PLUS Rounded 1c, sans-serif" font-weight="800" font-size="40" fill="var(--red)">1位65冠</text>
  </svg>
</div>
</body>
</html>
```